Tarrow Creek plumbing plumbing company business card design

Something sinilar to business card i upload it is my old business card design
And have a good watermark with the logo or majority of the logot in rhe background as watermark

Plumbing business similar to uploaded design with a nice watermark of the logo

Font styles to use
Script

Colors

Designer to choose colors to be used in the design.

```html
<!DOCTYPE html>
<html lang="en">
<head>
<meta charset="utf-8">
<title>Tarrow Creek Plumbing – Business Card</title>
<link rel="stylesheet" href="https://fonts.googleapis.com/css2?family=Arimo:wght@400;700&display=swap">
<style>
  :root {
    --backdrop: #3b3531;
    --card-black: #1c1c1d;
    --card-blue: #0a7acd;
    --watermark-blue: #0a6cb6;
    --ink-white: #ffffff;
    --ink-silver: #8d8e91;
    --rule-white: rgba(255,255,255,0.9);
  }
  * { box-sizing: border-box; margin: 0; padding: 0; }
  html, body {
    width: 1200px; height: 781px; overflow: hidden;
    background: var(--backdrop);
    font-family: "Arimo", Arial, sans-serif;
  }
  .stage { position: relative; width: 1200px; height: 781px; }
  .card {
    position: absolute; width: 560px; height: 320px;
    border-radius: 4px;
    box-shadow: 0 14px 30px rgba(0,0,0,0.45);
  }
  .card-front {
    left: 50px; top: 60px; background: var(--card-black);
    display: flex; align-items: center; justify-content: center;
  }
  .brand-name {
    font-weight: 700; text-transform: uppercase; letter-spacing: 4px;
  }
  .card-front .brand-name { color: var(--ink-silver); font-size: 30px; }
  .card-back {
    left: 590px; top: 400px; background: var(--card-blue);
    color: var(--ink-white); overflow: hidden;
  }
  .watermark {
    position: absolute; right: -18px; top: 60px;
    display: flex; flex-direction: column; align-items: flex-end;
    color: var(--watermark-blue);
    font-weight: 700; text-transform: uppercase;
    font-size: 78px; line-height: 82px; letter-spacing: 2px;
    pointer-events: none;
  }
  .card-back .brand-name {
    position: absolute; left: 34px; top: 34px; z-index: 1;
    font-size: 24px; color: var(--ink-white);
  }
  .person { position: absolute; left: 34px; top: 140px; z-index: 1; }
  .person-name { font-size: 22px; font-weight: 700; }
  .person-role { font-size: 13px; margin-top: 2px; }
  .person-rule {
    width: 150px; height: 2px; background: var(--rule-white); margin-top: 8px;
  }
  .contacts { position: absolute; left: 34px; top: 210px; list-style: none; z-index: 1; }
  .contacts li {
    display: flex; align-items: center; gap: 9px;
    font-size: 13px; line-height: 20px;
  }
  .contacts svg { width: 13px; height: 13px; fill: var(--ink-white); flex: none; }
  .divider {
    position: absolute; left: 34px; right: 34px; top: 280px; z-index: 1;
    height: 1px; background: var(--rule-white);
  }
  .licence {
    position: absolute; right: 34px; bottom: 12px; z-index: 1;
    font-size: 15px; font-weight: 700;
  }
</style>
</head>
<body>
<main class="stage">
  <section class="card card-front">
    <span class="brand-name">Tarrow Creek Plumbing</span>
  </section>

  <section class="card card-back">
    <div class="watermark" aria-hidden="true">
      <span>Tarrow</span>
      <span>Creek</span>
    </div>

    <span class="brand-name">Tarrow Creek Plumbing</span>

    <div class="person">
      <p class="person-name">Dario Mendel</p>
      <p class="person-role">Director</p>
      <div class="person-rule"></div>
    </div>

    <ul class="contacts">
      <li>
        <svg viewBox="0 0 24 24" aria-hidden="true"><path d="M6.6 10.8a15.1 15.1 0 0 0 6.6 6.6l2.2-2.2c.3-.3.7-.4 1-.2 1.1.4 2.3.6 3.6.6.6 0 1 .4 1 1V20c0 .6-.4 1-1 1A17 17 0 0 1 3 4c0-.6.4-1 1-1h3.5c.6 0 1 .4 1 1 0 1.3.2 2.5.6 3.6.1.3 0 .7-.2 1z"/></svg>
        0400 555 218
      </li>
      <li>
        <svg viewBox="0 0 24 24" aria-hidden="true"><path d="M2 5h20v14H2z M4 7v.5l8 5 8-5V7l-8 5z" fill-rule="evenodd"/></svg>
        info@tarrowcreekplumbing.com
      </li>
      <li>
        <svg viewBox="0 0 24 24" aria-hidden="true"><path d="M12 2a10 10 0 1 0 0 20 10 10 0 0 0 0-20zm6.9 6h-2.9a15.7 15.7 0 0 0-1.4-3.6A8 8 0 0 1 18.9 8zM12 4c.8 1.2 1.5 2.5 1.9 4h-3.8c.4-1.5 1.1-2.8 1.9-4zM4.3 14a8 8 0 0 1 0-4h3.4a16.5 16.5 0 0 0 0 4zm.8 2h2.9c.3 1.3.8 2.5 1.4 3.6A8 8 0 0 1 5.1 16zM8 8H5.1a8 8 0 0 1 4.3-3.6C8.8 5.5 8.3 6.7 8 8zm4 12c-.8-1.2-1.5-2.5-1.9-4h3.8c-.4 1.5-1.1 2.8-1.9 4zm2.3-6H9.7a14.7 14.7 0 0 1 0-4h4.6a14.7 14.7 0 0 1 0 4zm.3 5.6c.6-1.1 1.1-2.3 1.4-3.6h2.9a8 8 0 0 1-4.3 3.6zm1.7-5.6a16.5 16.5 0 0 0 0-4h3.4a8 8 0 0 1 0 4z"/></svg>
        tarrowcreekplumbing.com.au
      </li>
    </ul>

    <div class="divider"></div>
    <p class="licence">Lic No&nbsp; 480273C</p>
  </section>
</main>
</body>
</html>
```